Voyage Wellness Point Business Cards

We need business cards for our new start-up online travel health clinic. Visit our website voyagewellpoint.ca for branding and more info.

Target Market(s)

Travellers

Industry/Entity Type

Business

Contact Information for Business Card

Mara Kowalczyk
mara@voyagewellpoint.ca
+1 555 283 0461
voyagewellpoint.ca

Font styles to use
Sans Serif

Colors
f68d4d

```html
<!DOCTYPE html>
<html lang="en">
<head>
<meta charset="utf-8">
<title>Voyage Wellness Point – Business Cards</title>
<link rel="stylesheet" href="https://fonts.googleapis.com/css2?family=Open+Sans:wght@400;700&display=swap">
<style>
  :root {
    --brand-orange: #f4994f;
    --band-orange: #f68d4d;
    --ink: #1c1c1c;
    --rule: #e2e2e2;
    --paper: #ffffff;
    --bg-light: #d9d9d9;
    --bg-dark: #6e6e6e;
  }
  * { box-sizing: border-box; margin: 0; padding: 0; }
  html, body { width: 1200px; height: 1200px; overflow: hidden; }
  body {
    font-family: "Open Sans", sans-serif;
    background: radial-gradient(ellipse at 45% 55%, var(--bg-light) 0%, #a9a9a9 55%, var(--bg-dark) 100%);
    display: flex;
    flex-direction: column;
    align-items: center;
    justify-content: center;
    gap: 60px;
  }
  .card {
    width: 880px;
    height: 503px;
    position: relative;
    box-shadow: 6px 8px 14px rgba(0,0,0,0.35);
  }
  .wordmark {
    position: absolute;
    font-weight: 400;
    letter-spacing: -0.5px;
    line-height: 1.1;
    white-space: nowrap;
  }

  /* Front: white contact side */
  .card--contact { background: var(--paper); }
  .card--contact .wordmark {
    right: 40px;
    top: 78px;
    font-size: 46px;
    color: var(--brand-orange);
  }
  .card--contact .divider {
    position: absolute;
    left: 52px;
    right: 52px;
    top: 300px;
    height: 3px;
    background: var(--rule);
  }
  .holder-name {
    position: absolute;
    left: 50px;
    top: 338px;
    font-size: 30px;
    font-weight: 700;
    color: var(--ink);
  }
  .contact-list {
    position: absolute;
    left: 385px;
    top: 336px;
    list-style: none;
    font-size: 27px;
    line-height: 35px;
    color: var(--ink);
  }
  .contact-list li { display: flex; align-items: center; gap: 10px; }
  .contact-list svg { width: 22px; height: 22px; flex: none; }
  .card--contact .base-band {
    position: absolute;
    left: 0; right: 0; bottom: 0;
    height: 20px;
    background: var(--band-orange);
  }

  /* Back: orange brand side */
  .card--brand { background: var(--band-orange); }
  .card--brand .wordmark {
    right: 125px;
    top: 205px;
    font-size: 60px;
    color: var(--paper);
  }
</style>
</head>
<body>

  <section class="card card--contact" aria-label="Business card, contact side">
    <p class="wordmark">Voyage Wellness Point</p>
    <div class="divider"></div>
    <p class="holder-name">Mara Kowalczyk</p>
    <ul class="contact-list">
      <li>
        <svg viewBox="0 0 24 24" aria-hidden="true"><rect x="6" y="2" width="12" height="20" rx="2" fill="none" stroke="#f68d4d" stroke-width="2.4"/><circle cx="12" cy="18" r="1.4" fill="#f68d4d"/></svg>
        (555) 283-0461
      </li>
      <li>
        <svg viewBox="0 0 24 24" aria-hidden="true"><rect x="2" y="5" width="20" height="14" fill="none" stroke="#f68d4d" stroke-width="2.2"/><path d="M2 5l10 8 10-8" fill="none" stroke="#f68d4d" stroke-width="2.2"/></svg>
        mara@voyagewellpoint.ca
      </li>
      <li>
        <svg viewBox="0 0 24 24" aria-hidden="true"><circle cx="12" cy="12" r="10" fill="#f68d4d"/><path d="M2 12h20M12 2c-4 5-4 15 0 20M12 2c4 5 4 15 0 20" fill="none" stroke="#fff" stroke-width="1.2"/></svg>
        voyagewellpoint.ca
      </li>
    </ul>
    <div class="base-band"></div>
  </section>

  <section class="card card--brand" aria-label="Business card, brand side">
    <p class="wordmark">Voyage Wellness Point</p>
  </section>

</body>
</html>
```